Building certification business in Sydney Australia

Brookvale Assessors is a small business that is currently growing and needs a profession looking website to attract customers and give them all the information they need. The main services we offer currently are pre-purchase building inspections for purchasers and other areas of construction consultancy including pool fencing certificates. Please see attached logos to incorporate to also match colour schemes with. Thanks!

Target Market(s)

Prospective buyers and home owners

Industry/Entity Type

Small Business

Requirements
Must have
• Promote the main services from the home page. Being able to select the type of service/certificate required from the main page and be directed to a specific page that deals with only that service containing the relevant information for that item.
Nice to have
• Small emphasis on the location of our office and areas we service etc.

```html
<!DOCTYPE html>
<html lang="en">
<head>
<meta charset="utf-8">
<title>Brookvale Assessors – Building Certification Sydney</title>
<link rel="stylesheet" href="https://fonts.googleapis.com/css2?family=Source+Sans+3:ital,wght@0,400;0,600;1,400&family=Oswald:wght@400;600&family=Arimo:wght@400&display=swap">
<style>
  :root {
    --brand-blue: #1f7dc2;
    --brand-navy: #1c4f86;
    --link-blue: #1b78be;
    --text-dark: #333333;
    --text-mid: #555555;
    --text-soft: #6a6a6a;
    --rule: #d8d8d8;
    --band-grey: #f2f2f2;
    --footer-dark: #2b2b2b;
    --white: #ffffff;
    --social-blue-dark: #2d5aa0;
    --social-blue-light: #2a9ad8;
    --social-orange: #f0802a;
    --social-red: #d8302b;
  }
  * { box-sizing: border-box; margin: 0; padding: 0; }
  html, body { width: 707px; height: 1200px; overflow: hidden; }
  body {
    position: relative;
    background: var(--white);
    font-family: "Source Sans 3", sans-serif;
    color: var(--text-mid);
  }
  h1, h2, h3 { font-weight: 400; }

  /* Header */
  .site-header {
    position: absolute; left: 0; top: 0; width: 707px; height: 80px;
    background: linear-gradient(90deg, #f4f6f7 0%, #eef1ef 55%, #e3e9e2 100%);
  }
  .brand {
    position: absolute; left: 52px; top: 14px;
    display: flex; align-items: center; gap: 8px;
  }
  .brand-mark { width: 44px; height: 44px; background: var(--brand-navy); border-radius: 6px; }
  .brand-name {
    font-weight: 600; font-size: 20px; line-height: 21px; color: var(--brand-navy);
  }
  .main-nav { position: absolute; left: 300px; top: 0; display: flex; height: 80px; }
  .nav-item {
    width: 78px; height: 80px; text-align: center; padding-top: 27px;
    font-size: 11px; color: var(--text-dark); text-transform: uppercase;
  }
  .nav-item:first-child { width: 70px; }
  .nav-item small {
    display: block; font-size: 8.5px; font-style: italic; text-transform: none;
    color: #888; margin-top: 3px;
  }
  .nav-item.is-active { background: var(--brand-blue); color: var(--white); }
  .nav-item.is-active small { color: var(--white); }

  /* Hero */
  .hero {
    position: absolute; left: 0; top: 80px; width: 707px; height: 390px;
    background: linear-gradient(180deg, #5c8fc4 0%, #9fbad1 28%, #b9b2a3 50%, #6e8d3e 78%, #4d7a2a 100%);
  }
  .hero-caption {
    position: absolute; left: 368px; top: 185px; width: 290px; height: 105px;
    background: rgba(40, 36, 30, 0.55); padding: 14px 16px 0 17px; color: var(--white);
  }
  .hero-title { font-family: "Oswald", sans-serif; font-weight: 600; font-size: 18px; line-height: 22px; }
  .hero-subtitle { font-size: 13.5px; line-height: 17px; margin-top: 1px; }
  .hero-text { font-size: 9.5px; line-height: 14px; margin-top: 3px; }
  .hero-dots { position: absolute; right: 44px; bottom: 14px; display: flex; gap: 3px; }
  .hero-dots span { width: 10px; height: 10px; border-radius: 50%; background: rgba(255,255,255,0.5); }
  .hero-dots span:first-child { background: var(--white); }

  /* Services */
  .service-card {
    position: absolute; top: 510px; width: 182px; height: 172px;
    background: var(--white); border: 1px solid #dddddd;
    box-shadow: 0 6px 5px -4px rgba(0,0,0,0.35);
  }
  .service-media { margin: 4px; height: 89px; }
  .service-title { font-size: 11px; color: var(--link-blue); margin: 15px 0 0 7px; white-space: nowrap; }
  .service-text { font-size: 8.5px; line-height: 13px; color: var(--text-soft); margin: 6px 8px 0 7px; }

  /* Latest projects */
  .projects-band {
    position: absolute; left: 0; top: 750px; width: 707px; height: 300px;
    background: var(--band-grey);
  }
  .section-tab { position: absolute; left: 291px; top: 742px; width: 150px; height: 35px; }
  .section-tab-label {
    position: absolute; left: 0; top: 0; width: 150px; height: 35px; line-height: 35px;
    text-align: center; color: var(--white); font-size: 13.5px;
  }
  .projects-intro {
    position: absolute; left: 52px; top: 797px; width: 605px;
    text-align: center; font-size: 8.7px; line-height: 15px; color: var(--text-soft);
  }
  .project-card {
    position: absolute; top: 845px; width: 182px; height: 165px;
    background: var(--white); border: 1px solid #e2e2e2;
  }
  .project-card.is-hovered { border-bottom: 2px solid var(--brand-blue); }
  .project-media { margin: 4px; height: 99px; }
  .project-title {
    text-align: center; font-size: 11px; color: var(--link-blue);
    text-transform: uppercase; margin-top: 14px;
  }
  .project-text { text-align: center; font-size: 8.7px; color: var(--text-mid); margin-top: 6px; }

  /* Contact strip */
  .contact-strip {
    position: absolute; left: 0; top: 1050px; width: 707px; height: 79px; background: var(--white);
    box-shadow: inset 0 8px 8px -8px rgba(0,0,0,0.12);
  }
  .contact-item { position: absolute; top: 22px; display: flex; align-items: center; gap: 12px; font-family: "Arimo", sans-serif; }
  .contact-item p { font-size: 9.5px; color: var(--text-mid); line-height: 15px; }
  .contact-item .sub { font-size: 8.5px; color: var(--text-soft); }
  .contact-divider { position: absolute; top: 17px; width: 1px; height: 28px; background: var(--rule); }

  /* Footer */
  .site-footer {
    position: absolute; left: 0; top: 1129px; width: 707px; height: 71px;
    background: var(--footer-dark); font-family: "Arimo", sans-serif; color: var(--white);
  }
  .footer-links { position: absolute; left: 52px; top: 18px; font-size: 8.5px; }
  .footer-copy { position: absolute; left: 52px; top: 40px; font-size: 8.5px; }
  .social-list { position: absolute; left: 521px; top: 40px; display: flex; gap: 9px; }
  .social-list span { width: 21px; height: 21px; }
</style>
</head>
<body>

<header class="site-header">
  <div class="brand">
    <span class="brand-mark"></span>
    <span class="brand-name">Brookvale<br>Assessors</span>
  </div>
  <nav class="main-nav">
    <div class="nav-item is-active">Home<small>all starts here</small></div>
    <div class="nav-item">About us<small>adipiscing</small></div>
    <div class="nav-item">Services<small>Aenean masa</small></div>
    <div class="nav-item">Projects<small>commodgula</small></div>
    <div class="nav-item">Contact<small>sit amet</small></div>
  </nav>
</header>

<section class="hero" role="img" aria-label="Photo of a building inspector in a suit holding a folder in front of a suburban brick house with a lawn and trees">
  <div class="hero-caption">
    <h1 class="hero-title">THE DAYS OF BUYING EXPENSIVE</h1>
    <p class="hero-subtitle">DON'T BUY ANYMORE IN-STORE SERVICE</p>
    <p class="hero-text">Jerta baditaut onsequser untur magni dolores eoquie volup tate msequi nesciunt. Voluptatem accusantium dolorem.</p>
  </div>
  <div class="hero-dots"><span></span><span></span><span></span><span></span></div>
</section>

<article class="service-card" style="left:52px">
  <div class="service-media" role="img" aria-label="Illustration of a house beside an energy rating chart" style="background:linear-gradient(90deg,#3e9a3a 0%,#f2f2f2 45%,#f5c23a 70%,#e5452a 100%)"></div>
  <h2 class="service-title">Pre-purchase building inspections</h2>
  <p class="service-text">Claritas est etiam processus dynamicus, qui se quitur mutationem consuetudium lectorum.</p>
</article>
<article class="service-card" style="left:264px">
  <div class="service-media" role="img" aria-label="Photo of a swimming pool with glass fencing and timber deck" style="background:linear-gradient(100deg,#3fa7c9 0%,#7cc3d8 45%,#d9d2c4 60%,#9a4e2c 100%)"></div>
  <h2 class="service-title">Pool fencing certificates</h2>
  <p class="service-text">Claritas est etiam processus dynamicus, qui se quitur mutationem consuetudium lectorum.</p>
</article>
<article class="service-card" style="left:476px">
  <div class="service-media" role="img" aria-label="Photo of building plans, a hard hat and glasses with consultants in the background" style="background:linear-gradient(180deg,#e8eef3 0%,#c9d7e2 55%,#e9e2c8 80%,#f0c23a 100%)"></div>
  <h2 class="service-title">Pool fencing certificates</h2>
  <p class="service-text">Claritas est etiam processus dynamicus, qui se quitur mutationem consuetudium lectorum.</p>
</article>

<section class="projects-band" aria-labelledby="latest-projects"></section>
<div class="section-tab">
  <svg width="150" height="35" viewBox="0 0 150 35" aria-hidden="true">
    <polygon points="0,8 8,0 8,8" fill="#0f5b92"/>
    <polygon points="150,8 142,0 142,8" fill="#0f5b92"/>
    <rect x="8" y="0" width="134" height="35" fill="#1f7dc2"/>
  </svg>
  <h2 class="section-tab-label" id="latest-projects">Latest Projects</h2>
</div>
<p class="projects-intro">Mirum est notare quam littera gothica, quam nunc putamus parum claram, anteposuerit litterarum formas humanitatis per seacula quarta decima et quinta decima.<br>Eodem modo typi, qui nunc nobis videntur parum clari, fiant sollemnes in futurum. Mirum est notare quam littera gothica, quam nunc putamus parum .</p>

<article class="project-card is-hovered" style="left:52px">
  <div class="project-media" role="img" aria-label="Photo of a farmhouse with a silo behind a white fence" style="background:linear-gradient(180deg,#9cbfe0 0%,#c4d2dc 45%,#8a9a88 65%,#5f7f3a 100%)"></div>
  <h3 class="project-title">Donec nec justo ege fs</h3>
  <p class="project-text">Donec nec justo eget felis facilisis fermtum .</p>
</article>
<article class="project-card" style="left:264px">
  <div class="project-media" role="img" aria-label="Photo of a two-storey suburban home with a front lawn" style="background:linear-gradient(180deg,#3f7fc6 0%,#8fb6de 35%,#c7b79c 60%,#5d8a34 100%)"></div>
  <h3 class="project-title">Donec nec justo ege fs</h3>
  <p class="project-text">Donec nec justo eget felis facilisis fermtum .</p>
</article>
<article class="project-card" style="left:476px">
  <div class="project-media" role="img" aria-label="Photo of hands holding house keys and a small model house" style="background:linear-gradient(100deg,#dcdcdc 0%,#d9b7a0 40%,#c85a3e 65%,#e2e2e2 100%)"></div>
  <h3 class="project-title">Donec nec justo ege fs</h3>
  <p class="project-text">Donec nec justo eget felis facilisis fermtum .</p>
</article>

<section class="contact-strip">
  <div class="contact-item" style="left:52px">
    <svg width="16" height="22" viewBox="0 0 16 22" aria-hidden="true">
      <path d="M8 0C3.6 0 0 3.5 0 7.9 0 13.5 8 22 8 22s8-8.5 8-14.1C16 3.5 12.4 0 8 0z" fill="#3a3a3a"/>
      <circle cx="8" cy="8" r="3" fill="#fff"/>
    </svg>
    <div><p>Duis autem vel eum iriureHendrerit.</p><p class="sub">Typi non habent claritatem insitam</p></div>
  </div>
  <span class="contact-divider" style="left:272px"></span>
  <div class="contact-item" style="left:322px;top:24px">
    <svg width="18" height="18" viewBox="0 0 24 24" aria-hidden="true">
      <path d="M6.6 10.8c1.4 2.8 3.8 5.1 6.6 6.6l2.2-2.2c.3-.3.7-.4 1-.2 1.1.4 2.3.6 3.6.6.6 0 1 .4 1 1V20c0 .6-.4 1-1 1C10.6 21 3 13.4 3 4c0-.6.4-1 1-1h3.5c.6 0 1 .4 1 1 0 1.3.2 2.5.6 3.6.1.3 0 .7-.2 1l-2.3 2.2z" fill="#3a3a3a"/>
    </svg>
    <p>123 - 456 - 789</p>
  </div>
  <span class="contact-divider" style="left:459px"></span>
  <div class="contact-item" style="left:507px;top:25px">
    <svg width="27" height="17" viewBox="0 0 27 17" aria-hidden="true">
      <rect width="27" height="17" fill="#3a3a3a"/>
      <polyline points="1,1 13.5,10 26,1" fill="none" stroke="#fff" stroke-width="1.5"/>
    </svg>
    <p>info@brookvalemail.com</p>
  </div>
</section>

<footer class="site-footer">
  <p class="footer-links">Terms and Conditions | Privacy Promise | FAQ's | Contact Us</p>
  <p class="footer-copy">Copyright © 2013. All Rights Reserved.</p>
  <div class="social-list" aria-label="Social links">
    <span style="background:var(--social-blue-dark)"></span>
    <span style="background:var(--social-blue-light)"></span>
    <span style="background:var(--social-orange)"></span>
    <span style="background:var(--social-red)"></span>
  </div>
</footer>

</body>
</html>
```